Baby Adoption Announcement

I'm looking for a simple, understated and modern baby adoption announcement.

The baby is a boy, but I don't want anything that is blue or particularly boyish. No storks, baby baskets, rattles, or traditional baby announcement designs. No cutesy or busy designs.

Should measure 5.25 x 8.25 inches to fit in an A9 envelope.

Simple graphics MIGHT include birds, grasses, trees, rivers. I'm open to other ideas. Text can be a single color or multi colored. Graphics are not mandatory.

Since this is text heavy, I'd like the designer to be REALLY GOOD at choosing fonts and typesetting.

Text should read:

Memory answers us bright on your face—
Impossibly, we spoke and were silent
Together before all of this. (in italics)

Cornelius Tobias Pelter Quist
Born on March 16, 2012 in Boston, MA
and entrusted to us by his birthmother, Gwenda.

Named Cornelius, which means God is with us, after Gwenda’s grandfather &
Tobias, after Toby and St. Tobias of Karvel

• Should measure 5.25 x 8.25 inches to fit in A9 envelope.

• The baby is a boy, but I don't want anything that is blue or particularly boyish. No storks, baby baskets, rattles, or traditional baby announcement designs. Nothing cutesy or busy.

```html
<!DOCTYPE html>
<html lang="en">
<head>
<meta charset="utf-8">
<title>Adoption Announcement – Cornelius Tobias Pelter Quist</title>
<link href="https://fonts.googleapis.com/css2?family=Petit+Formal+Script&family=Marcellus&family=Marcellus+SC&display=swap" rel="stylesheet">
<style>
  :root {
    --paper: #ffffff;
    --frame-olive: #a29b6c;
    --frame-brown: #8a5527;
    --frame-navy: #465471;
    --divider: #d6d6d6;
    --stamp-grey: #d9d9d9;
    --ink-brown: #7b4a1e;
    --ink-dark: #6a3c12;
    --ink-olive: #9b9468;
  }
  * { margin: 0; padding: 0; box-sizing: border-box; }
  html, body {
    width: 1200px; height: 801px; overflow: hidden; background: var(--paper);
  }
  .card { position: relative; width: 1200px; height: 801px; background: var(--paper); }
  .card-frames { position: absolute; inset: 0; }
  .stamp-label {
    position: absolute; left: 147px; top: 407px;
    transform: translate(-50%, -50%) rotate(90deg);
    font-family: "Marcellus SC", serif; font-size: 26px; letter-spacing: 2px;
    color: var(--stamp-grey);
  }
  .message {
    position: absolute; left: 297px; right: 44px; top: 0; bottom: 0;
    text-align: center; color: var(--ink-brown);
  }
  .message > * { position: absolute; left: 0; right: 0; transform: translateY(-50%); }
  .welcome { top: 127px; font-family: "Petit Formal Script", cursive; font-size: 36px; }
  .poem { top: 268px; font-family: "Petit Formal Script", cursive; font-size: 27px; line-height: 46px; }
  .baby-name { top: 393px; font-family: "Marcellus SC", serif; font-size: 31px; letter-spacing: 1px; color: var(--ink-dark); }
  .birth-details { top: 488px; font-family: "Marcellus", serif; font-size: 21px; line-height: 42px; }
  .naming { top: 626px; font-family: "Marcellus", serif; font-size: 21px; line-height: 42px; }
  .birthmother { font-family: "Petit Formal Script", cursive; font-size: 25px; color: var(--ink-olive); }
  .meaning { font-family: "Marcellus SC", serif; font-size: 24px; color: var(--ink-olive); }
  .caps { font-family: "Marcellus SC", serif; font-size: 23px; }
</style>
</head>
<body>
<main class="card">
  <svg class="card-frames" width="1200" height="801" viewBox="0 0 1200 801" aria-hidden="true">
    <rect x="13" y="13" width="1174" height="775" rx="32" fill="none" stroke="var(--frame-olive)" stroke-width="7"/>
    <rect x="29" y="29" width="1142" height="743" rx="26" fill="none" stroke="var(--frame-brown)" stroke-width="7"/>
    <rect x="45" y="45" width="1110" height="711" rx="20" fill="none" stroke="var(--frame-navy)" stroke-width="7"/>
    <line x1="297" y1="49" x2="297" y2="752" stroke="var(--divider)" stroke-width="2"/>
  </svg>

  <div class="stamp-label">Stamp</div>

  <section class="message">
    <h1 class="welcome">We Welcome with Joy</h1>
    <p class="poem">Memory answers us bright on your face<br>Impossibly, we spoke and were silent<br>Together before all of this</p>
    <h2 class="baby-name">Cornelius Tobias Pelter Quist</h2>
    <p class="birth-details">Born on March 16, 2012 in Boston, MA<br>and entrusted to us by his birthmother, <span class="birthmother">Gwenda.</span></p>
    <p class="naming">Named CORNELIUS, which means <span class="meaning">God is with us</span><br>after Gwenda’s grandfather &amp;<br><span class="caps">Tobias</span>, after Toby and <span class="caps">St. Tobias of Karvel</span></p>
  </section>
</main>
</body>
</html>
```